Free IT Diploma Flyer Design Project

Our training company needs a flashy flyer to promote our exceptional offer ,
Free Registration
Free laptop /vexo /torlin slate
Free Internet
Guaranteed Job
International Recognition
Get your Qualification in Shortest Possible Time
Save a year on Bachelor Degree , Go straight to 2nd Year Uni
Still thinking you bloody idiot
Get Enrolled start your career now
We are seeking talented & Creative Designer to show his skills to catch our target market , all age groups , male & female . The Design should match the offer.
Training

```html
<!DOCTYPE html>
<html lang="en">
<head>
<meta charset="utf-8">
<title>nexalearn – Free IT Diploma Flyer</title>
<link rel="stylesheet" href="https://fonts.googleapis.com/css2?family=Oswald:wght@600;700&family=Roboto+Condensed:wght@700&family=Roboto:wght@400;500;700&display=swap">
<style>
  :root {
    --navy: #0b2f7a;
    --navy-deep: #082463;
    --blue: #1167d6;
    --blue-bright: #2a8cf0;
    --blue-mid: #0d4fb8;
    --lime: #cbdc2a;
    --white: #ffffff;
    --ink: #0e1f3e;
  }
  * { margin: 0; padding: 0; box-sizing: border-box; }
  html, body { width: 856px; height: 1200px; overflow: hidden; background: #e9edf3; }
  .flyer {
    position: relative;
    width: 856px; height: 1200px; overflow: hidden;
    background: radial-gradient(ellipse at 35% 30%, var(--blue-bright) 0%, var(--blue) 45%, var(--blue-mid) 100%);
    font-family: "Roboto", Arial, sans-serif;
    color: var(--white);
  }
  .backdrop { position: absolute; inset: 0; }

  /* header */
  .top-strip {
    position: absolute; left: 0; top: 0; width: 856px; height: 86px;
    background: linear-gradient(90deg, var(--blue-mid), var(--blue));
  }
  .brand-tab {
    position: absolute; left: 0; top: 0; width: 333px; height: 121px;
    background: var(--navy); border-radius: 0 0 22px 22px;
    display: flex; align-items: center; justify-content: center;
  }
  .brand-name { font-family: "Roboto", Arial, sans-serif; font-weight: 500; font-size: 46px; color: var(--white); letter-spacing: -0.5px; }
  .top-perk {
    position: absolute; top: 28px;
    font-family: "Roboto Condensed", Arial, sans-serif; font-weight: 700; font-size: 19px;
    display: flex; align-items: center; gap: 10px; letter-spacing: 0.3px;
  }
  .bullet { width: 17px; height: 17px; background: var(--lime); border-radius: 2px; flex: none; }
  .lime-tab { position: absolute; top: 86px; height: 28px; background: var(--lime); border-radius: 0 0 16px 16px; }

  /* headline */
  .headline {
    position: absolute; left: 68px; top: 172px;
    font-family: "Oswald", Impact, sans-serif; font-weight: 700;
    font-size: 62px; line-height: 73px; letter-spacing: 0.2px;
    text-shadow: 0 3px 6px rgba(0,0,0,0.35);
  }
  .headline .accent { color: var(--lime); }

  /* perk bars */
  .perk-bar {
    position: absolute; left: 452px; width: 404px; height: 53px;
    background: linear-gradient(90deg, #0a3d99, var(--navy-deep));
    display: flex; align-items: center; gap: 14px; padding-left: 38px;
    font-family: "Roboto Condensed", Arial, sans-serif; font-weight: 700; font-size: 18px;
    box-shadow: 0 3px 8px rgba(0,0,0,0.25);
  }

  .saving { position: absolute; left: 70px; top: 570px; font-size: 22px; line-height: 31px; }
  .saving b { font-weight: 700; }

  .web-band {
    position: absolute; left: 44px; top: 679px; width: 400px; height: 57px;
    background: linear-gradient(90deg, rgba(8,36,99,0) 0%, var(--navy-deep) 14%, var(--navy-deep) 86%, rgba(8,36,99,0) 100%);
    display: flex; align-items: center; justify-content: center;
    font-weight: 700; font-size: 30px; color: var(--lime);
  }
  .web-band .domain { color: var(--white); }
  .phone { position: absolute; left: 96px; top: 749px; display: flex; align-items: center; gap: 8px; font-weight: 700; font-size: 31px; }

  .cap-photo {
    position: absolute; left: 60px; top: 921px; width: 290px; height: 158px;
    background: radial-gradient(ellipse at 55% 45%, #2a2a2a 0%, #555 40%, rgba(255,255,255,0) 72%);
  }
  .person-photo {
    position: absolute; left: 470px; top: 540px; width: 330px; height: 660px;
    background: linear-gradient(180deg, rgba(255,255,255,0.35) 0%, #1a1c24 28%, #0d0e14 100%);
    border-radius: 120px 120px 0 0;
  }

  .footer-bar {
    position: absolute; left: 0; top: 1125px; width: 856px; height: 75px;
    background: linear-gradient(90deg, var(--navy), #1049a8 60%, var(--navy));
    display: flex; align-items: center; padding-left: 58px;
    font-weight: 700; font-size: 23px;
  }
</style>
</head>
<body>
<main class="flyer">
  <svg class="backdrop" width="856" height="1200" viewBox="0 0 856 1200" aria-hidden="true">
    <path d="M0 830 C 250 880, 520 860, 856 760 L 856 1200 L 0 1200 Z" fill="#0a3590"/>
    <path d="M0 800 C 260 840, 560 810, 856 700" stroke="#cbdc2a" stroke-width="10" fill="none"/>
    <path d="M0 820 C 260 870, 560 840, 856 735" stroke="#082463" stroke-width="26" fill="none"/>
    <path d="M0 852 C 280 890, 600 860, 856 790 L 856 1000 C 640 1080, 320 1100, 0 1090 Z" fill="#ffffff"/>
    <path d="M300 1125 C 520 1070, 700 1040, 856 990" stroke="#cbdc2a" stroke-width="10" fill="none"/>
    <path d="M0 1070 C 300 1100, 620 1060, 856 1010 L 856 1125 L 0 1125 Z" fill="#1459c6"/>
  </svg>

  <header>
    <div class="top-strip"></div>
    <div class="brand-tab"><span class="brand-name">nexalearn</span></div>
    <div class="top-perk" style="left:361px"><span class="bullet"></span>FREE REGISTRATION</div>
    <div class="top-perk" style="left:612px"><span class="bullet"></span>GUARANTEED JOB</div>
    <div class="lime-tab" style="left:364px; width:223px"></div>
    <div class="lime-tab" style="left:598px; width:211px"></div>
  </header>

  <h1 class="headline">Get your<br><span class="accent">Qualification</span><br>in Shortest<br>Possible<br>Time!</h1>

  <div class="perk-bar" style="top:258px"><span class="bullet"></span>FREE INTERNET</div>
  <div class="perk-bar" style="top:328px"><span class="bullet"></span>INTERNATIONAL RECOGNITION</div>
  <div class="perk-bar" style="top:398px"><span class="bullet"></span>FREE LAPTOP /VEXO /TORLIN SLATE</div>

  <p class="saving"><b>Save a year</b> on Bachelor Degree,<br>Go straight to <b>2nd Year Uni!</b></p>

  <div class="web-band">www.<span class="domain">nexalearn</span>.net.au</div>
  <div class="phone">
    <svg width="34" height="26" viewBox="0 0 34 26" aria-hidden="true">
      <path d="M2 9 C 6 2, 28 2, 32 9 L 32 12 L 25 12 L 24 8 L 10 8 L 9 12 L 2 12 Z" fill="#cbdc2a"/>
      <path d="M7 13 L 27 13 L 30 24 L 4 24 Z" fill="#cbdc2a"/>
      <circle cx="17" cy="18" r="3.5" fill="#1167d6"/>
    </svg>
    1300 555 014
  </div>

  <div class="cap-photo" role="img" aria-label="Photo of a graduation cap with a rolled diploma tied in red ribbon"></div>
  <div class="person-photo" role="img" aria-label="Photo of a smiling businesswoman in a black suit holding a laptop"></div>

  <footer class="footer-bar">Get Enrolled start your career now!</footer>
</main>
</body>
</html>
```